Presentation Brochure and Sample Box Design for Veto Sheet

Veto Sheet is a colour coated solid aluminium panel that our company supplies to the signage and building cladding industries.
We require an, A4 double-sided folding brochure (swatch book) that folds 3 ways, opening once and then a second time to lay out 3 pages flat.

There should be a front and back cover.

The inside cover should be reserved with text blocks for written information about the panel.

The opposite page on the right when you first open the brochure should have all our Matte PVDF 2mm colours which you will find in the attached PDF of colour swatches and details.

When the brochure is folded out a second time, showing all three inside pages flat, the two inside pages on the right (next to the inside cover with the written information) should show all our FEVE Gloss 1.6mm colours which you will also find in the attached PDF colour book.

This brochure should have a modern and professional feel suitable for presenting to architects and designers.

We also require a box design to contain aluminium samples of all the colours in the range.

Please refer to the template attached for the box dimensions and layout.

The box should tie in with the brochure as a complete package with a modern and professional look suitable for presenting to architects and designers.

Finally we require a small label sticker to be stuck on the back of each sample. On the sticker should be the Veto Sheet logo, a space to put the product code for the sample colour and the phone number 1300 584 396.

To summarise, this package project includes:
1 tri-folding A4 brochure,
1 sample box package design,
1 sample sticker label.

This is our signature new product that we will be marketing to signage installers to create coloured and printed aluminium signs. We are also looking to move further into the building and architectural market place with this product.

Please refer to the attachments for the Veto Sheet logo - the colour swatch book and template for the sample box.
The Veto Sheet logo can be shown in White, Black or Silver.

Target Market(s)

Architects, interior designers, builders and signage installers.

Font styles to use
Serif
Sans Serif

Requirements
Must have
• A modern, neat and professional upmarket look suitable for presenting to architects.
Nice to have
• A slick and classy look that makes you want to take home the box or brochure even if you're not interested in the product.
Should not have
• A cheap, untidy, low market look with too many colours.

```html
<!DOCTYPE html>
<html lang="en">
<head>
<meta charset="utf-8">
<title>Veto Sheet – Colour Swatch Brochure</title>
<link rel="stylesheet" href="https://fonts.googleapis.com/css2?family=Libre+Baskerville&family=Lato:wght@300;400;700&display=swap">
<style>
  :root{
    --backdrop:#939393;
    --paper:#ffffff;
    --band:#c5c9d0;
    --ink:#2b2b2b;
    --rule:#9a9a9a;
    --soft-grey:#8a8c8f;
    --silver:#a9abae;
    --serif:"Libre Baskerville", Georgia, serif;
    --sans:"Lato", Arial, sans-serif;
  }
  *{box-sizing:border-box;margin:0;padding:0}
  html,body{width:901px;height:1200px;overflow:hidden;background:var(--backdrop)}
  .stage{position:absolute;left:0;top:0;width:1660px;height:2212px;transform:scale(0.54277);transform-origin:0 0;font-family:var(--sans);color:var(--ink)}
  .sheet{position:absolute;left:134px;width:1393px;height:986px;background:var(--paper)}
  .sheet--outside{top:120px}
  .sheet--inside{top:1148px}
  .panel{position:absolute;top:0;height:100%;width:464px}
  .panel--band{left:464px;background:var(--band)}
  .panel--cover{left:928px}

  .heading{position:absolute;width:416px;border-bottom:1.5px solid var(--rule);padding-bottom:10px}
  .heading .kicker{font-family:var(--serif);font-size:25px;line-height:30px;color:#111}
  .heading .range{font-family:var(--sans);font-size:24px;line-height:28px;color:#111;letter-spacing:.3px}

  .swatches{position:absolute;display:grid;grid-template-columns:repeat(4,92px);column-gap:13.5px}
  .chip{height:var(--row,135px)}
  .tile{display:block;width:92px;height:92px;border-radius:14px;background:var(--c);box-shadow:0 0 0 1.5px #e4e4e4}
  .name{display:block;margin-top:13px;font-size:11px;line-height:12px;text-transform:uppercase;color:#222}
  .name.mixed{text-transform:none}
  .name small{font-size:11px;text-transform:uppercase}

  .wordmark{position:absolute;font-family:var(--sans);font-weight:400;letter-spacing:4px;white-space:nowrap}
  .contact{position:absolute;left:0;width:464px;top:840px;text-align:center;color:#fff;font-size:16px;font-weight:300;line-height:20px}

  .cover-photo{position:absolute;left:20px;top:4px}
  .cover-note{position:absolute;left:236px;top:607px;width:212px;height:212px;border-radius:50%;background:rgba(150,152,155,.85);color:#fff;font-size:15px;line-height:20px;font-weight:300;text-align:center;padding:43px 22px 0}
  .cover-title{position:absolute;left:0;width:464px;top:842px;text-align:center;font-size:30px;font-weight:300;color:var(--soft-grey);letter-spacing:.5px}
  .cover-sub{position:absolute;left:0;width:464px;top:880px;text-align:center;font-family:var(--serif);font-size:15px;color:var(--soft-grey);letter-spacing:1.2px}
</style>
</head>
<body>
<div class="stage">

  <!-- Outside spread -->
  <section class="sheet sheet--outside">
    <div class="panel">
      <div class="heading" style="left:24px;top:38px">
        <p class="kicker">Colour coated solid aluminium</p>
        <p class="range">PVDF MATTE 2MM</p>
      </div>
      <div class="swatches" style="left:28px;top:141px">
        <div class="chip"><span class="tile" style="--c:#fff"></span><span class="name">White</span></div>
        <div class="chip"><span class="tile" style="--c:#050507"></span><span class="name">Black</span></div>
        <div class="chip"><span class="tile" style="--c:#d21f33"></span><span class="name">Red</span></div>
        <div class="chip"><span class="tile" style="--c:#283680"></span><span class="name">Reflex Blue</span></div>
        <div class="chip"><span class="tile" style="--c:#f15a29"></span><span class="name">Orange</span></div>
        <div class="chip"><span class="tile" style="--c:#11244a"></span><span class="name">Navy Blue</span></div>
        <div class="chip"><span class="tile" style="--c:#1b2658"></span><span class="name">Galaxy</span></div>
        <div class="chip"><span class="tile" style="--c:#e4d4ab"></span><span class="name">Ivory</span></div>
        <div class="chip"><span class="tile" style="--c:#fbb226"></span><span class="name">Mustard</span></div>
        <div class="chip"><span class="tile" style="--c:#c31f33"></span><span class="name">Plum Red</span></div>
        <div class="chip"><span class="tile" style="--c:#333d48"></span><span class="name">Steel Grey</span></div>
        <div class="chip"><span class="tile" style="--c:#5e6872"></span><span class="name">Iron Grey</span></div>
        <div class="chip"><span class="tile" style="--c:#a4a7aa"></span><span class="name">Warm Grey</span></div>
        <div class="chip"><span class="tile" style="--c:#c6c8cb"></span><span class="name">Smokey Grey</span></div>
        <div class="chip"><span class="tile" style="--c:#d9d5cf"></span><span class="name">Cream</span></div>
        <div class="chip"></div>
        <div class="chip"><span class="tile" style="--c:radial-gradient(circle,#d2d2d2,#b5b5b5)"></span><span class="name">Metallic<br>Silver</span></div>
        <div class="chip"><span class="tile" style="--c:radial-gradient(circle,#5a5a5a,#444)"></span><span class="name">Metallic<br>Charcoal</span></div>
        <div class="chip"><span class="tile" style="--c:radial-gradient(circle,#c4a672,#b59760)"></span><span class="name">Metallic<br>Gold</span></div>
        <div class="chip"><span class="tile" style="--c:radial-gradient(circle,#e9d93a,#dcc92a)"></span><span class="name">Metallic<br>Yellow</span></div>
        <div class="chip"><span class="tile" style="--c:radial-gradient(circle,#1a6cc0,#0e56a6)"></span><span class="name">Metallic<br>Blue</span></div>
      </div>
    </div>

    <div class="panel panel--band">
      <p class="wordmark" style="left:0;width:464px;text-align:center;top:760px;font-size:48px;color:#fff">VETO SHEET</p>
      <div class="contact">
        <p>1300 584 396</p>
        <p>48 Harbour Lane, Northgate</p>
        <p>www.vetosheet-panels.com</p>
      </div>
    </div>

    <div class="panel panel--cover">
      <svg class="cover-photo" width="426" height="816" viewBox="0 0 426 816" role="img" aria-label="Photograph of a building facade clad in faceted triangular aluminium panels with glazing">
        <defs>
          <linearGradient id="facade" x1="0" y1="0" x2="1" y2="1">
            <stop offset="0" stop-color="#d7d9db"/>
            <stop offset=".45" stop-color="#a9acaf"/>
            <stop offset=".7" stop-color="#7f8488"/>
            <stop offset="1" stop-color="#c5c7c9"/>
          </linearGradient>
        </defs>
        <polygon points="0,0 208,118 128,250 60,330 0,390" fill="url(#facade)"/>
        <polygon points="326,196 426,256 426,816 0,816 0,700 120,560 210,420 290,270" fill="url(#facade)"/>
      </svg>
      <p class="cover-note">Aluminium panels refers to a covering used on one material for providing protection as well as decorative look.</p>
      <p class="wordmark" style="left:222px;top:26px;font-size:34px;color:var(--silver)">VETO SHEET</p>
      <p class="cover-title">ALUMINIUM PANELS</p>
      <p class="cover-sub">A new trend in the construction</p>
    </div>
  </section>

  <!-- Inside spread -->
  <section class="sheet sheet--inside">
    <div class="panel">
      <div class="heading" style="left:24px;top:58px">
        <p class="kicker">Colour coated solid aluminium</p>
        <p class="range">FEVE GLOSS 1.6MM</p>
      </div>
      <div class="swatches" style="left:26px;top:145px;--row:137px">
        <div class="chip"><span class="tile" style="--c:#fff"></span><span class="name">White</span></div>
        <div class="chip"><span class="tile" style="--c:#060607"></span><span class="name">Black</span></div>
        <div class="chip"><span class="tile" style="--c:#d21f33"></span><span class="name">Red</span></div>
        <div class="chip"><span class="tile" style="--c:#f4ee25"></span><span class="name">Yellow</span></div>
        <div class="chip"><span class="tile" style="--c:#1c87c4"></span><span class="name">Process Blue</span></div>
        <div class="chip"><span class="tile" style="--c:#283679"></span><span class="name">Reflex Blue</span></div>
        <div class="chip"><span class="tile" style="--c:#134734"></span><span class="name">Forest Green</span></div>
        <div class="chip"><span class="tile" style="--c:#802231"></span><span class="name">Heritage Red</span></div>
        <div class="chip"><span class="tile" style="--c:#f15a29"></span><span class="name">Orange</span></div>
        <div class="chip"><span class="tile" style="--c:#f3823a"></span><span class="name">Pumpkin</span></div>
        <div class="chip"><span class="tile" style="--c:#102750"></span><span class="name">Navy Blue</span></div>
        <div class="chip"><span class="tile" style="--c:#074f80"></span><span class="name">Lagoon</span></div>
        <div class="chip"><span class="tile" style="--c:#1a2356"></span><span class="name">Galaxy</span></div>
        <div class="chip"><span class="tile" style="--c:#0b7b8c"></span><span class="name">Turquoise</span></div>
        <div class="chip"><span class="tile" style="--c:#18a24a"></span><span class="name">Green</span></div>
        <div class="chip"><span class="tile" style="--c:#e5d6ab"></span><span class="name">Ivory</span></div>
        <div class="chip"><span class="tile" style="--c:#12984c"></span><span class="name">Emerald</span></div>
        <div class="chip"><span class="tile" style="--c:#3fb04b"></span><span class="name">Apple Green</span></div>
        <div class="chip"><span class="tile" style="--c:#ee3342"></span><span class="name">Warm Red</span></div>
        <div class="chip"><span class="tile" style="--c:#fbb326"></span><span class="name">Mustard</span></div>
        <div class="chip"><span class="tile" style="--c:#8440a0"></span><span class="name">Violet</span></div>
        <div class="chip"><span class="tile" style="--c:#9cc942"></span><span class="name">Lime Green</span></div>
        <div class="chip"><span class="tile" style="--c:#66aa45"></span><span class="name">Spring Green</span></div>
        <div class="chip"><span class="tile" style="--c:#ec1c7a"></span><span class="name">Fuchsia</span></div>
      </div>
    </div>

    <div class="panel" style="left:466px">
      <div class="heading" style="left:24px;top:58px">
        <p class="kicker">Colour coated solid aluminium</p>
        <p class="range">FEVE GLOSS 1.6MM</p>
      </div>
      <div class="swatches" style="left:26px;top:145px;--row:137px">
        <div class="chip"><span class="tile" style="--c:#c31f33"></span><span class="name">Plum Red</span></div>
        <div class="chip"><span class="tile" style="--c:#eb98c3"></span><span class="name">Pink</span></div>
        <div class="chip"><span class="tile" style="--c:#333d48"></span><span class="name">Steel Grey</span></div>
        <div class="chip"><span class="tile" style="--c:#118a80"></span><span class="name">Mint</span></div>
        <div class="chip"><span class="tile" style="--c:#12535a"></span><span class="name">Teal</span></div>
        <div class="chip"><span class="tile" style="--c:#6b3a35"></span><span class="name">Milk Chocolate</span></div>
        <div class="chip"><span class="tile" style="--c:#f9e03d"></span><span class="name">Lemon Meringue</span></div>
        <div class="chip"><span class="tile" style="--c:#0c4f95"></span><span class="name">Patriotic Blue</span></div>
        <div class="chip"><span class="tile" style="--c:#93c8e9"></span><span class="name">Baby Blue</span></div>
        <div class="chip"><span class="tile" style="--c:#5b8373"></span><span class="name">Olive Green</span></div>
        <div class="chip"><span class="tile" style="--c:#5e6873"></span><span class="name">Iron Grey</span></div>
        <div class="chip"><span class="tile" style="--c:#a3a7aa"></span><span class="name">Warm Grey</span></div>
        <div class="chip"><span class="tile" style="--c:#c7c9cc"></span><span class="name">Smokey Grey</span></div>
        <div class="chip"><span class="tile" style="--c:#b9ada3"></span><span class="name">Latte</span></div>
        <div class="chip"><span class="tile" style="--c:#9c8f87"></span><span class="name">Stone</span></div>
        <div class="chip"><span class="tile" style="--c:#7f6f67"></span><span class="name">Mocha</span></div>
        <div class="chip"><span class="tile" style="--c:#5c4a4a"></span><span class="name">Aubergine</span></div>
        <div class="chip"><span class="tile" style="--c:#413b66"></span><span class="name">Midnight Purple</span></div>
        <div class="chip"><span class="tile" style="--c:#f7982a"></span><span class="name">Feve Matte<br>Tangerine</span></div>
        <div class="chip"><span class="tile" style="--c:#828b94"></span><span class="name mixed">High gloss<br><small>Ash</small></span></div>
        <div class="chip"><span class="tile" style="--c:#dbd7d0"></span><span class="name mixed">High gloss<br><small>Cream</small></span></div>
        <div class="chip"><span class="tile" style="--c:#62292e"></span><span class="name">Rust</span></div>
        <div class="chip"><span class="tile" style="--c:#1e1a4f"></span><span class="name mixed">Feve<br><small>Royal Blue</small></span></div>
        <div class="chip"><span class="tile" style="--c:#6a389a"></span><span class="name mixed">Feve <small>Violet</small></span></div>
      </div>
    </div>

    <div class="panel" style="left:925px">
      <div class="heading" style="left:24px;top:58px">
        <p class="kicker">Colour coated solid aluminium</p>
        <p class="range">FEVE GLOSS 1.6MM</p>
      </div>
      <div class="swatches" style="left:28px;top:147px">
        <div class="chip"><span class="tile" style="--c:#3e2e82"></span><span class="name">Feve Purple</span></div>
        <div class="chip"><span class="tile" style="--c:#a5238e"></span><span class="name">Feve Mulberry</span></div>
      </div>
      <div class="heading" style="left:30px;top:322px">
        <p class="kicker">Colour coated solid aluminium</p>
        <p class="range">METALLICS &amp; PEARLS 1.6MM</p>
      </div>
      <div class="swatches" style="left:28px;top:413px;--row:140px;column-gap:16.5px">
        <div class="chip"><span class="tile" style="--c:radial-gradient(circle,#c2b8b0,#aea39a)"></span><span class="name mixed">Feve metallic<br><small>Champagne</small></span></div>
        <div class="chip"><span class="tile" style="--c:radial-gradient(circle,#cfae70,#b8975a)"></span><span class="name mixed">Feve metallic<br><small>Gold</small></span></div>
        <div class="chip"><span class="tile" style="--c:radial-gradient(circle,#d4d4d6,#b7b8ba)"></span><span class="name mixed">Feve metallic<br><small>Flash Silver</small></span></div>
        <div class="chip"><span class="tile" style="--c:linear-gradient(120deg,#8d9088,#c9cbc6 50%,#8f928c)"></span><span class="name mixed">Feve metallic<br><small>Silver</small></span></div>
        <div class="chip"><span class="tile" style="--c:#050505"></span><span class="name mixed">Feve metallic<br><small>Black</small></span></div>
        <div class="chip"><span class="tile" style="--c:linear-gradient(135deg,#c06020,#f4b07a 45%,#e27a2c 75%)"></span><span class="name mixed">Feve pearl<br><small>Copper</small></span></div>
        <div class="chip"><span class="tile" style="--c:radial-gradient(circle,#5a5a5c,#3e3e40)"></span><span class="name mixed">Feve pearl<br><small>White</small></span></div>
        <div class="chip"><span class="tile" style="--c:radial-gradient(circle,#d3d3d3,#b9b9b9)"></span><span class="name mixed">Feve pearl<br><small>Latte</small></span></div>
        <div class="chip"><span class="tile" style="--c:linear-gradient(135deg,#8e8880,#c9c3bb 50%,#9a948c)"></span><span class="name mixed">Feve pearl<br><small>Ocean Grey</small></span></div>
        <div class="chip"><span class="tile" style="--c:linear-gradient(135deg,#9aa3ab,#d4d9dd 50%,#a9b1b8)"></span><span class="name mixed">Feve pearl<br><small>Blue Grey</small></span></div>
        <div class="chip"><span class="tile" style="--c:linear-gradient(135deg,#9fb8cc,#dde7ef 50%,#a9c1d3)"></span><span class="name mixed">Feve metallic<br><small>Champagne</small></span></div>
        <div class="chip"><span class="tile" style="--c:linear-gradient(135deg,#a8673e,#e8c9a0 50%,#b57a4f)"></span><span class="name mixed">Feve metallic<br><small>Brass Gold</small></span></div>
      </div>
      <p class="wordmark" style="left:160px;top:868px;font-size:46px;color:#111">VETO SHEET</p>
    </div>
  </section>

</div>
</body>
</html>
```